Redesign our company's business card. HSG BUSINESS CARD 2015

We are an Audio Visual Production company with a flare of marketing and sales. Lights camera ACTION!! We are Production and creative designers and thinkers whom provide first class service for many vantage 300 companies that Exhibit at trade shows and sales meetings.

Double sided, sleek, fashionable, and modern.

www.halvernstudio.com

Think ZNQ'S Crestline

Target Market(s)

Trade Show Mangers, Event coordinators, Project managers,

Industry/Entity Type

Marketing

Contact Information for Business Card

Name Tile, Logo, Slogan, photos of our work on the back. Chatterly and blipper

Font styles to use
Sans Serif
Decorative
Script

Colors
33a6d7
ffffff
0692cd
cee9f5

Requirements
Must have
• Multi color, professional, Upscale,
• CREATING GREAT PARTNERSHIPS THAT PRODUCE AMAZING RESULTS
Nice to have
• Photos of our work on the back
Should not have
• Address or fax.

```html
<!DOCTYPE html>
<html lang="en">
<head>
<meta charset="utf-8">
<title>HSG Business Card</title>
<link rel="stylesheet" href="https://fonts.googleapis.com/css2?family=Open+Sans:wght@400;600;700&display=swap">
<style>
  :root {
    --page-bg: #e9edf0;
    --card-white: #ffffff;
    --brand-blue: #0692cd;
    --brand-sky: #33a6d7;
    --brand-deep: #1f6fb8;
    --brand-mist: #cee9f5;
    --ink-name: #1d4f8f;
    --ink-body: #4a4f55;
    --swoosh-light: #f4f5f6;
    --swoosh-dark: #b9bec3;
  }
  * { margin: 0; padding: 0; box-sizing: border-box; }
  html, body {
    width: 1200px; height: 901px; overflow: hidden;
    background: var(--page-bg);
    font-family: "Open Sans", Arial, sans-serif;
  }
  .business-card {
    position: absolute; left: 100px; top: 165px;
    width: 1000px; height: 571px;
    border-radius: 48px; overflow: hidden;
    background: var(--card-white);
    box-shadow: 0 10px 30px rgba(0,0,0,.15);
  }
  .card-art { position: absolute; inset: 0; }
  .brand-mark {
    position: absolute; left: 56px; top: 52px;
    display: flex; align-items: center; gap: 18px;
    color: var(--brand-sky); font-weight: 600;
  }
  .brand-dot {
    width: 92px; height: 92px; border-radius: 50%;
    background: var(--brand-blue);
  }
  .brand-text { display: flex; flex-direction: column; }
  .brand-name { font-size: 64px; line-height: 1; letter-spacing: 6px; }
  .brand-full { font-size: 16px; letter-spacing: 3px; text-transform: uppercase; margin-top: 6px; }
  .person { position: absolute; left: 80px; top: 190px; }
  .person-name {
    font-size: 22px; font-weight: 700; color: var(--ink-name);
    text-transform: uppercase; letter-spacing: .5px;
  }
  .person-title { font-size: 16px; color: var(--ink-body); margin-top: 2px; }
  .contact-list {
    position: absolute; left: 80px; top: 262px;
    list-style: none; font-size: 15px; color: var(--ink-body);
  }
  .contact-list li { display: flex; align-items: center; gap: 12px; height: 27px; }
  .contact-list svg { width: 15px; height: 15px; fill: var(--ink-name); flex: none; }
  .slogan {
    position: absolute; left: 80px; top: 440px; width: 460px;
    font-size: 13px; font-weight: 600; line-height: 1.5;
    letter-spacing: 1.5px; text-transform: uppercase;
    color: var(--brand-sky);
  }
</style>
</head>
<body>
  <section class="business-card" aria-label="HSG business card front">
    <svg class="card-art" viewBox="0 0 1000 571" preserveAspectRatio="none" aria-hidden="true">
      <defs>
        <linearGradient id="blueBand" x1="0" y1="0" x2="1" y2="1">
          <stop offset="0" stop-color="var(--brand-sky)"/>
          <stop offset=".55" stop-color="var(--brand-blue)"/>
          <stop offset="1" stop-color="var(--brand-deep)"/>
        </linearGradient>
        <linearGradient id="swoosh" x1="0" y1="0" x2="0" y2="1">
          <stop offset="0" stop-color="var(--swoosh-light)"/>
          <stop offset="1" stop-color="var(--swoosh-dark)"/>
        </linearGradient>
      </defs>
      <rect class="blue-band" width="1000" height="571" fill="url(#blueBand)"/>
      <path class="grey-swoosh" d="M770 0 C905 110 905 430 650 571 H520 C780 470 880 150 770 0 Z" fill="url(#swoosh)"/>
      <path class="white-face" d="M0 0 H770 C880 150 780 470 520 571 H0 Z" fill="var(--card-white)"/>
    </svg>

    <div class="brand-mark">
      <span class="brand-dot"></span>
      <div class="brand-text">
        <span class="brand-name">HSG</span>
        <span class="brand-full">Halvern Studio Group</span>
      </div>
    </div>

    <div class="person">
      <p class="person-name">Marcus Ellery</p>
      <p class="person-title">Managing Director</p>
    </div>

    <ul class="contact-list">
      <li><svg viewBox="0 0 16 16"><path d="M4 1h8v14H4z M5.5 2.5v10h5v-10z"/></svg>012 555 0147</li>
      <li><svg viewBox="0 0 16 16"><path d="M3 2l3 0 1 3-2 1c1 2 3 4 5 5l1-2 3 1v3c-6 0-11-5-11-11z"/></svg>012 555 0147</li>
      <li><svg viewBox="0 0 16 16"><path d="M1 3h14v10H1z M2 4l6 5 6-5z" fill-rule="evenodd"/></svg>hello@halvernstudio.com</li>
      <li><svg viewBox="0 0 16 16"><circle cx="8" cy="8" r="7"/></svg>www.halvernstudio.com</li>
    </ul>

    <p class="slogan">Creating Great Partnerships<br>That Produce Amazing Results</p>
  </section>
</body>
</html>
```